Business Card Design Project

We are a very talented award winning hair salon, the card should be professional, classy with edge. Attached is the logo which I would like to see on one side, with text and something catchy on back.

Target Market(s)

Young professional, 20-50

Industry/Entity Type

Hair

Colors

Designer to choose colors to be used in the design.

Requirements
Must have
• Must be clean, exude professionalism, classy with some edge

```html
<!DOCTYPE html>
<html lang="en">
<head>
<meta charset="utf-8">
<title>Élan Salon – Business Cards</title>
<link rel="stylesheet" href="https://fonts.googleapis.com/css2?family=Cormorant+Garamond:wght@500&family=Cormorant+SC:wght@500&display=swap">
<style>
  :root {
    --page: #e9e6e1;
    --card-black: #050505;
    --gold: #d4a62a;
    --ink-light: #f2f2f2;
    --ink-dark: #111111;
    --photo-warm-a: #c9b8a8;
    --photo-warm-b: #6e5a4c;
    --photo-cool-a: #f4f6f8;
    --photo-cool-b: #b9c0c7;
  }
  * { box-sizing: border-box; margin: 0; padding: 0; }
  html, body {
    width: 1200px; height: 764px; overflow: hidden;
    background: var(--page);
  }
  .sheet { position: relative; width: 1200px; height: 764px; }
  .card {
    position: absolute; width: 540px; height: 309px;
    border-radius: 24px; overflow: hidden;
    box-shadow: 0 4px 14px rgba(0,0,0,.18);
  }
  .card--black { background: var(--card-black); }
  .card--contact { left: 40px; top: 53px; }
  .card--stylist { left: 620px; top: 53px; }
  .card--tagline { left: 40px; top: 402px; }
  .card--interior { left: 620px; top: 402px; }

  .photo { position: absolute; inset: 0; }
  .photo--stylist { background: linear-gradient(120deg, var(--photo-warm-a) 0%, #e8e2dc 45%, var(--photo-warm-b) 100%); }
  .photo--interior { background: linear-gradient(180deg, var(--photo-cool-a) 0%, #e3e7ea 55%, var(--photo-cool-b) 100%); }

  .brand {
    position: absolute; white-space: nowrap;
    font-family: "Cormorant Garamond", serif; font-weight: 500;
    letter-spacing: .12em; color: var(--gold);
  }
  .brand--dark { color: var(--ink-dark); }

  .card--contact .brand { left: 40px; top: 52px; font-size: 44px; }
  .contact {
    position: absolute; left: 40px; bottom: 26px;
    font-family: "Cormorant SC", serif; font-weight: 500;
    color: var(--ink-light); font-size: 15px; line-height: 1.35;
  }
  .contact__name { font-size: 18px; margin-bottom: 4px; }
  .contact__address { margin-top: 6px; }

  .tagline {
    position: absolute; font-family: "Cormorant Garamond", serif;
    font-weight: 500; white-space: nowrap;
  }
  .card--stylist .tagline { left: 22px; top: 40px; font-size: 19px; color: var(--ink-dark); }
  .card--stylist .brand { left: 22px; top: 74px; font-size: 28px; }

  .card--tagline .brand { left: 0; right: 0; top: 86px; text-align: center; font-size: 56px; }
  .card--tagline .tagline { left: 0; right: 0; top: 206px; text-align: center; font-size: 28px; color: var(--ink-light); }

  .card--interior .tagline { left: 0; right: 0; top: 22px; text-align: center; font-size: 27px; color: var(--ink-dark); }
  .card--interior .brand { left: 0; right: 0; top: 222px; text-align: center; font-size: 32px; }
</style>
</head>
<body>
<main class="sheet">

  <section class="card card--black card--contact">
    <div class="brand">ÉLAN SALON</div>
    <div class="contact">
      <p class="contact__name">Your Name, Title</p>
      <p>P: 123-456-7980</p>
      <p>F: 123-568-7896</p>
      <p>E: elansalon@example.com</p>
      <p class="contact__address">Street Name City Name, State ZipCode</p>
    </div>
  </section>

  <section class="card card--stylist">
    <div class="photo photo--stylist" role="img" aria-label="Smiling stylist trimming a client's brown hair in a bright salon"></div>
    <p class="tagline">The Ultimate Indulgent Hair Experience</p>
    <div class="brand brand--dark">ÉLAN SALON</div>
  </section>

  <section class="card card--black card--tagline">
    <div class="brand">ÉLAN SALON</div>
    <p class="tagline">The Ultimate Indulgent Hair Experience</p>
  </section>

  <section class="card card--interior">
    <div class="photo photo--interior" role="img" aria-label="Bright white salon interior with styling chairs and mirrors"></div>
    <p class="tagline">The Ultimate Indulgent Hair Experience</p>
    <div class="brand brand--dark">ÉLAN SALON</div>
  </section>

</main>
</body>
</html>
```